Business card design needed

I need a business card for my new Food & Lifestyle Coaching business - "Bloomvale Food & Lifestlye Coaching"

i already have a logo and would like to have that incorporated into the business card, obviously.

i would like a design that says "fresh" and "funky" - my target market is female, aged 20-45 so i want something that will stand out to them when they see it.

My "Company Colour" is Apple Green
Updates

Thankyou to everyone who has submitted a design for my project. At this stage i have quite a large number of designs to chose from and with only a short time until my project closes i am focusing now on chosing from those i have already shortlisted so am unfortunately not considering any new desings.

Thankyou again for your interest in my project.

Target Market(s)

Female, Health Conscious (or looking to improve their health/lifestyle), aged between 20-45

Industry/Entity Type

Business

Contact Information for Business Card

Tamsin Corley
Ph: 0417382946
Email: eatwell@marovex.com

Requirements
Must have
• Must include my existing Logo
Nice to have
• Would be nice to incoirporate and appointment card on the back

```html
<!DOCTYPE html>
<html lang="en">
<head>
<meta charset="utf-8">
<title>Bloomvale Food &amp; Lifestlye Coaching – Business &amp; Appointment Card</title>
<link rel="stylesheet" href="https://fonts.googleapis.com/css2?family=Open+Sans:wght@400;600;700&display=swap">
<style>
  :root {
    --apple-green: #9ac22e;
    --apple-green-soft: #cfe39a;
    --apple-green-pale: #e6f1c6;
    --ink: #2d2d2d;
    --rule: #b9b9b9;
    --card: #ffffff;
    --backdrop: #e9ecee;
  }
  * { box-sizing: border-box; margin: 0; padding: 0; }
  html, body {
    width: 1200px; height: 960px; overflow: hidden;
    background: var(--backdrop);
    font-family: "Open Sans", Arial, sans-serif;
    color: var(--ink);
  }
  .card {
    position: absolute; left: 240px; width: 720px; height: 430px;
    background: var(--card);
    box-shadow: 0 6px 22px rgba(0,0,0,.12);
    overflow: hidden;
  }
  .card--front { top: 40px; }
  .card--back  { top: 490px; }

  /* Front */
  .brand {
    position: absolute; left: 44px; top: 40px;
    display: flex; align-items: center; gap: 16px;
  }
  .brand__dot {
    width: 58px; height: 58px; border-radius: 50%;
    background: var(--apple-green);
  }
  .brand__name {
    font-weight: 400; color: var(--ink); line-height: 1.1;
  }
  .brand__name .brand__word { display: block; font-size: 46px; letter-spacing: -.5px; }
  .brand__name .brand__line { display: block; font-size: 15px; margin-top: 4px; }

  .band {
    position: absolute; background: var(--apple-green);
  }
  .band--name {
    left: 0; top: 186px; width: 630px; height: 58px;
    clip-path: polygon(0 0, 100% 0, 94% 100%, 0 100%);
  }
  .band--contact {
    right: 0; top: 272px; width: 560px; height: 62px;
    clip-path: polygon(5% 0, 100% 0, 100% 100%, 0 100%);
  }
  .holder-name {
    position: absolute; left: 94px; top: 196px;
    font-size: 30px; font-weight: 400; color: var(--ink);
  }
  .motif {
    position: absolute; border-radius: 40% 60% 45% 55%;
    background: radial-gradient(circle at 40% 40%, var(--apple-green-soft), var(--apple-green));
  }
  .motif--band-end { left: 620px; top: 166px; width: 62px; height: 62px; }
  .motif--contact  { left: 176px; top: 262px; width: 66px; height: 70px; }

  .contact {
    position: absolute; top: 290px; display: flex; align-items: center; gap: 10px;
    font-size: 19px; color: var(--ink);
  }
  .contact--phone { left: 262px; }
  .contact--email { left: 440px; font-size: 17px; }
  .contact svg { flex: none; }

  /* Back */
  .appointment__title {
    position: absolute; top: 26px; left: 0; width: 100%;
    text-align: center; font-size: 15px; font-weight: 700; letter-spacing: 1px;
  }
  .appointment__lines {
    position: absolute; left: 66px; right: 54px; top: 72px;
    list-style: none;
  }
  .appointment__lines li {
    height: 38px; border-bottom: 1px solid var(--rule);
  }
  .trail {
    position: absolute; left: 90px; top: 8px; width: 560px; height: 400px;
    background: radial-gradient(ellipse at 30% 25%, rgba(154,194,46,.35), rgba(154,194,46,0) 55%),
                radial-gradient(ellipse at 60% 60%, rgba(154,194,46,.4), rgba(154,194,46,0) 50%);
    border-radius: 40%;
  }
</style>
</head>
<body>

  <section class="card card--front" aria-label="Business card front">
    <div class="brand">
      <span class="brand__dot" aria-hidden="true"></span>
      <p class="brand__name">
        <span class="brand__word">Bloomvale</span>
        <span class="brand__line">Food &amp; Lifestlye Coaching</span>
      </p>
    </div>

    <div class="band band--name"></div>
    <div class="motif motif--band-end" role="img" aria-label="Green leaf-wing motif"></div>
    <h1 class="holder-name">Tamsin Corley</h1>

    <div class="band band--contact"></div>
    <div class="motif motif--contact" role="img" aria-label="Green leaf-wing motif"></div>

    <p class="contact contact--phone">
      <svg width="14" height="22" viewBox="0 0 14 22" aria-hidden="true">
        <rect x="1" y="1" width="12" height="20" rx="2" fill="none" stroke="#2d2d2d" stroke-width="2"/>
        <rect x="3.5" y="4" width="7" height="6" fill="#2d2d2d"/>
        <circle cx="7" cy="16" r="1.6" fill="#2d2d2d"/>
      </svg>
      0417382946
    </p>
    <p class="contact contact--email">
      <svg width="20" height="15" viewBox="0 0 20 15" aria-hidden="true">
        <rect x="1" y="1" width="18" height="13" fill="none" stroke="#2d2d2d" stroke-width="1.6"/>
        <path d="M1 1 L10 8 L19 1" fill="none" stroke="#2d2d2d" stroke-width="1.6"/>
      </svg>
      eatwell@marovex.com
    </p>
  </section>

  <section class="card card--back" aria-label="Appointment card back">
    <div class="trail" role="img" aria-label="Trail of soft green leaf-wing shapes drifting across the card"></div>
    <h2 class="appointment__title">NEXT APPOINTMENT</h2>
    <ul class="appointment__lines" aria-hidden="true">
      <li></li><li></li><li></li><li></li><li></li><li></li><li></li><li></li><li></li>
    </ul>
  </section>

</body>
</html>
```